Greek Yogurt Design

Design Brief – Premium Greek Yogurt Line (150g Pot)
Background
We are a small-to-medium dairy producer launching a new premium Greek yogurt range. This line will come in slightly larger pots than our standard yogurts, and we are targeting an upmarket clientele with a higher price point.
Product Details
Product: Greek Yogurt (fruit on the bottom, yogurt on top)
Flavours:
Natural
Strawberry
Forest Fruit
Peach & Apricot
Vanilla
Mango
Weight: 150g
Kosher Certification: 2 logos must be applied neatly (logos provided).
Lid: Standard universal lid (not flavour-specific).
Design Style
Clean, elegant, and premium feel (avoid clutter).
Should stand out as sophisticated compared to our standard range.
Visual hierarchy:
Brand & product type (Greek Yogurt) should be clear.
Flavour indicated with subtle but distinct cues (colour palette, fruit illustration/photography).
“Fruit on the bottom” message should be communicated simply.
Premium cues: minimalist typography, restrained colour palette, elegant fruit imagery.
References / Inspiration
Velmora Yogurt
– clean, bold, dairy-traditional.
Brask Dairy Greek Style
– natural, elegant design.
Lunaro Greek Yogurt
– modern, colourful yet clean.
Deliverables
Pot sleeve / pot design (to wrap around container).
Must work across all flavours with colour/flavour variation.
Space for universal lid (do not design individual lids).
Application of 2 kosher logos in a balanced way.
Updates
Industry/Entity Type
Dairy
Colors
Designer to choose colors to be used in the design.
Look and feel
Each slider illustrates characteristics of the customer's brand and the style your logo design should communicate.

```html
<!DOCTYPE html>
<html lang="en">
<head>
<meta charset="utf-8">
<title>Greek Yogurt Pot Sleeves</title>
<link href="https://fonts.googleapis.com/css2?family=Kaushan+Script&family=Grandstander:wght@700&family=Mali:wght@500;700&family=Nunito:wght@800&display=swap" rel="stylesheet">
<style>
  :root {
    --stage: #858484;
    --stage-dark: #5f5e5e;
    --sleeve-white: #ffffff;
    --brand-green: #3aa336;
    --brand-green-dark: #2f6e3a;
    --ink: #1c1c1c;
    --straw-band: #e88a8f;
    --straw-band-light: #f6c9cb;
    --straw-base: #d8222a;
    --straw-text: #d3232b;
    --straw-fruit: #e2474d;
    --peach-band: #e9b98f;
    --peach-band-light: #f8e6d3;
    --peach-base: #efc9a4;
    --peach-line: #e0352c;
    --peach-text: #f47a62;
    --peach-fruit: #f39a3b;
    --badge: #d7d7d7;
  }
  * { margin: 0; padding: 0; box-sizing: border-box; }
  html, body { width: 1200px; height: 735px; overflow: hidden; }
  body {
    background: linear-gradient(180deg, var(--stage) 0%, var(--stage-dark) 100%);
    position: relative;
  }
  .sleeve {
    position: absolute;
    top: 160px;
    width: 520px;
    height: 420px;
    background: var(--sleeve-white);
    border-radius: 10px;
    overflow: hidden;
  }
  .sleeve--strawberry { left: 50px; }
  .sleeve--peach { left: 630px; }
  .sleeve__top-band {
    position: absolute; left: 0; top: 0; width: 100%; height: 70px;
  }
  .sleeve--strawberry .sleeve__top-band {
    background: linear-gradient(180deg, var(--straw-band) 0%, var(--straw-band-light) 60%, var(--sleeve-white) 100%);
  }
  .sleeve--peach .sleeve__top-band {
    background: linear-gradient(180deg, var(--peach-band) 0%, var(--peach-band-light) 60%, var(--sleeve-white) 100%);
  }
  .sleeve__base-band {
    position: absolute; left: 0; bottom: 0; width: 100%; height: 54px;
  }
  .sleeve--strawberry .sleeve__base-band {
    background: var(--straw-base);
    border-top: 4px solid var(--brand-green);
  }
  .sleeve--peach .sleeve__base-band {
    background: var(--peach-base);
    border-top: 4px solid var(--peach-line);
  }
  .mascot {
    position: absolute; left: 165px; top: 58px; width: 84px; height: 68px;
    border-radius: 34px 34px 40px 40px;
    background: linear-gradient(180deg, #e9e9e9 0%, #f1c6c6 100%);
  }
  .brand {
    position: absolute; left: 272px; top: 78px;
    font-family: "Nunito", sans-serif; font-weight: 800; font-size: 30px; line-height: 1;
    color: var(--brand-green);
  }
  .product-type {
    position: absolute; left: 0; top: 132px; width: 100%;
    text-align: center;
    font-family: "Kaushan Script", cursive; font-size: 64px; line-height: 1;
    color: var(--brand-green);
  }
  .fruit {
    position: absolute; top: 200px; width: 80px; height: 100px; border-radius: 36px;
  }
  .fruit--left { left: 10px; }
  .fruit--right { right: 10px; }
  .sleeve--strawberry .fruit { background: radial-gradient(circle, var(--straw-fruit) 0%, rgba(226,71,77,0.25) 70%, rgba(255,255,255,0) 100%); }
  .sleeve--peach .fruit { background: radial-gradient(circle, var(--peach-fruit) 0%, rgba(243,154,59,0.25) 70%, rgba(255,255,255,0) 100%); }
  .flavour {
    position: absolute; left: 0; top: 220px; width: 100%; text-align: center;
    font-family: "Grandstander", sans-serif; font-weight: 700; font-size: 34px; line-height: 1;
  }
  .sleeve--strawberry .flavour { color: var(--straw-text); }
  .sleeve--peach .flavour { color: var(--peach-text); }
  .tagline {
    position: absolute; left: 0; top: 272px; width: 100%; text-align: center;
    font-family: "Mali", sans-serif; font-weight: 500; font-size: 22px; line-height: 1.2; color: var(--ink);
  }
  .weight {
    position: absolute; left: 0; top: 306px; width: 100%; text-align: center;
    font-family: "Mali", sans-serif; font-weight: 700; font-size: 20px; line-height: 1.2; color: var(--ink);
  }
  .cert {
    position: absolute; top: 282px; width: 40px; height: 40px; border-radius: 50%;
    background: var(--badge);
  }
  .cert--left { left: 92px; }
  .cert--right { right: 92px; }
</style>
</head>
<body>
  <section class="sleeve sleeve--strawberry">
    <div class="sleeve__top-band"></div>
    <div class="mascot" role="img" aria-label="Cartoon cow mascot illustration"></div>
    <div class="brand">Melkara</div>
    <h1 class="product-type">Greek Yogurt</h1>
    <div class="fruit fruit--left" role="img" aria-label="Scattered strawberry photographs"></div>
    <div class="fruit fruit--right" role="img" aria-label="Scattered strawberry photographs"></div>
    <h2 class="flavour">Strawberry</h2>
    <p class="tagline">Fruit On The Bottom</p>
    <p class="weight">150G</p>
    <div class="cert cert--left" role="img" aria-label="Kosher certification badge"></div>
    <div class="cert cert--right" role="img" aria-label="Kosher certification badge"></div>
    <div class="sleeve__base-band"></div>
  </section>

  <section class="sleeve sleeve--peach">
    <div class="sleeve__top-band"></div>
    <div class="mascot" role="img" aria-label="Cartoon cow mascot illustration"></div>
    <div class="brand">Melkara</div>
    <h1 class="product-type">Greek Yogurt</h1>
    <div class="fruit fruit--left" role="img" aria-label="Scattered peach and apricot photographs"></div>
    <div class="fruit fruit--right" role="img" aria-label="Scattered peach and apricot photographs"></div>
    <h2 class="flavour">Peach &amp; Apricot</h2>
    <p class="tagline">Fruit On The Bottom</p>
    <p class="weight">150G</p>
    <div class="cert cert--left" role="img" aria-label="Kosher certification badge"></div>
    <div class="cert cert--right" role="img" aria-label="Kosher certification badge"></div>
    <div class="sleeve__base-band"></div>
  </section>
</body>
</html>
```